■依頼の目的/概要
大阪・北新地でホテルやレストラン向け青果卸と小売りをしています。
コロナの影響でレストラン向け卸が苦戦する中、
新たに個人向け事業として、
オンラインショップと配膳堂での配達を始めました。
その案内DMの作成をお願いいたします。

■依頼詳細
デザイン案
弊社の説明
オンラインショップ、配膳堂、ピクモ、TALQアカウントのQRコード
を入れていただきたいです。
ロゴ、QRコード、商品の写真などは添付ファイルの通りです。
枚数
5000枚
サイズ
はがきサイズ
(配達地域指定郵便での発送を考えております。)

■要望点
上記のとおり、ロゴ等は添付ファイルのものを使用して頂きます。
一般的なスーパーでは手に入らない野菜や調味料などを販売しており、
スタイリッシュなイメージを希望しています。
弊社ピクモ、通販ページなどをご参考ください。
https://hanamori.kaimono-box.jp

その他何かご不明な点がございましたら、お気軽にご質問下さい。
よろしくお願いいたします。

```html
<!DOCTYPE html>
<html lang="ja">
<head>
<meta charset="utf-8">
<title>花森 オンラインショップ・配膳堂 ご案内はがき</title>
<link rel="stylesheet" href="https://fonts.googleapis.com/css2?family=Noto+Serif+JP:wght@400;500;700&family=Cormorant+Garamond:wght@500;600&display=swap">
<style>
  :root {
    --paper: #ffffff;
    --ink: #2a2a2a;
    --ink-soft: #4a4a4a;
    --rule: #555555;
    --green: #5d9e34;
    --badge: #5f9f36;
    --logo-bg: #2b2b2b;
  }
  html, body {
    margin: 0;
    padding: 0;
    overflow: hidden;
    background: #eeeeee;
  }
  .postcard {
    position: relative;
    width: 806px;
    height: 1200px;
    background: var(--paper);
    color: var(--ink);
    font-family: "Noto Serif JP", serif;
    overflow: hidden;
  }
  .postcard-label {
    position: absolute;
    top: 26px;
    left: 0;
    width: 100%;
    text-align: center;
    font-family: "Cormorant Garamond", serif;
    font-size: 17px;
    letter-spacing: 1px;
    color: var(--ink-soft);
  }
  .postage-box {
    position: absolute;
    top: 54px;
    left: 80px;
    width: 212px;
    height: 160px;
    border: 1.5px solid var(--rule);
    box-sizing: border-box;
  }
  .postage-box .postage-title {
    height: 44px;
    line-height: 44px;
    text-align: center;
    font-size: 21px;
    letter-spacing: 2px;
    border-bottom: 1.5px solid var(--rule);
  }
  .postage-box .brand-name {
    margin: 14px auto 0;
    width: 170px;
    height: 84px;
    background: var(--logo-bg);
    color: #ffffff;
    font-family: "Cormorant Garamond", serif;
    font-weight: 600;
    font-size: 24px;
    letter-spacing: 3px;
    display: flex;
    align-items: center;
    justify-content: center;
  }
  .delivery-zone {
    position: absolute;
    top: 254px;
    left: 100px;
    writing-mode: vertical-rl;
    font-size: 29px;
    font-weight: 500;
    letter-spacing: 5px;
  }
  .produce-photo {
    position: absolute;
    top: 490px;
    left: 0;
    width: 806px;
    height: 232px;
    background: linear-gradient(100deg, #b9352c 0%, #d96a2a 14%, #6f8d3c 30%, #3f6e2b 48%, #9bb45a 62%, #e9e5d6 74%, #5b8a34 86%, #c43b2f 100%);
  }
  .founded-badge {
    position: absolute;
    top: 614px;
    left: 578px;
    width: 168px;
    height: 168px;
    border-radius: 50%;
    background: var(--badge);
    color: #ffffff;
    display: flex;
    flex-direction: column;
    align-items: center;
    justify-content: center;
    font-size: 22px;
    font-weight: 500;
    line-height: 1.45;
    letter-spacing: 1px;
  }
  .message {
    position: absolute;
    top: 770px;
    left: 0;
    width: 100%;
    text-align: center;
  }
  .shop-intro {
    margin: 0;
    font-size: 25px;
    font-weight: 700;
    letter-spacing: 1px;
  }
  .headline {
    margin: 22px 0 0;
    color: var(--green);
    font-size: 42px;
    font-weight: 700;
    line-height: 1.38;
    letter-spacing: 1px;
  }
  .description {
    margin: 34px 0 0;
    font-size: 18.5px;
    line-height: 1.75;
    color: var(--ink-soft);
  }
  .company {
    margin: 30px 0 0;
    font-size: 18px;
    line-height: 1.7;
    color: var(--ink-soft);
  }
</style>
</head>
<body>
  <main class="postcard">
    <div class="postcard-label">POST CARD</div>

    <div class="postage-box">
      <div class="postage-title">料金後納郵便</div>
      <div class="brand-name">HANAMORI</div>
    </div>

    <div class="delivery-zone">配達地域指定</div>

    <div class="produce-photo" role="img" aria-label="色とりどりのこだわり野菜が並ぶ写真"></div>

    <div class="founded-badge">
      <span>北新地で</span>
      <span>創業74年</span>
    </div>

    <section class="message">
      <p class="shop-intro">こだわり野菜の八百屋 北新地「花森」</p>
      <h1 class="headline">「オンラインショップ」＆「配膳堂」<br>はじめました。</h1>
      <p class="description">
        当社では、一般的なスーパーでは手に入らない野菜や果物、調味料などを<br>
        販売しております。旬の野菜や果物、カレーや鍋などのレシピに合わせたセット商品や、<br>
        ギフトにぴったりなこだわりセット商品も取り揃えております。
      </p>
      <p class="company">
        株式会社花森<br>
        〒530-0002 大阪府 大阪市北区曽根崎新地9-9-9
      </p>
    </section>
  </main>
</body>
</html>
```